luxury contemporary fashion website needs simple, elegant flowchart to describe the buying and selli

* Luxury, resale, preloved items are sold on this online platform
*Horizontal, simple, flowchart with 5 steps in 'friendly' font with a simple emoticon/ picture for each step
*To be positioned in the 'How we work' tab of the webpage to explain in a very simple manner the buying and selling process for the customers.
*Attached is a very rudimentary mock-up of what we would like included and an idea of a project similar to what we desire
* to confirm the text for each step, we have also attached a word file below

Industry/Entity Type

Fashion

Font styles to use
Sans Serif

Colors
86cfc6
cfeae6

Requirements
Must have
• Simple drawing / shape after each point In the closest to 'duck egg blue' fill colour you can find with a black outline

```html
<!DOCTYPE html>
<html lang="en">
<head>
<meta charset="utf-8">
<title>Bespoke Concierge Service – How we work</title>
<link rel="stylesheet" href="https://fonts.googleapis.com/css2?family=Archivo+Black&family=Open+Sans:wght@400;600&family=Oswald:wght@600&display=swap">
<style>
  :root {
    --duck-egg: #86cfc6;
    --duck-egg-pale: #cfeae6;
    --duck-egg-mist: #e7f5f3;
    --duck-egg-deep: #4f9e95;
    --teal-ink: #2b6a63;
    --charcoal: #1e2626;
    --outline: #111111;
    --card-white: #ffffff;
    --ink: #2a2a2a;
  }
  * { box-sizing: border-box; margin: 0; padding: 0; }
  html, body { width: 1200px; height: 483px; overflow: hidden; background: var(--duck-egg-mist); }
  .canvas {
    position: relative; width: 1200px; height: 483px; overflow: hidden;
    background: linear-gradient(180deg, var(--duck-egg-pale) 0, var(--duck-egg-pale) 96px, var(--duck-egg-mist) 96px, var(--duck-egg-mist) 462px, var(--duck-egg-deep) 462px, var(--duck-egg-deep) 465px, var(--duck-egg-pale) 465px);
    font-family: "Open Sans", sans-serif;
  }
  .title { position: absolute; top: 13px; left: 341px; width: 547px; display: flex; height: 49px; }
  .title span {
    font-family: "Archivo Black", sans-serif; color: #fff; font-size: 27px;
    line-height: 49px; letter-spacing: 0.2px; text-align: center; white-space: nowrap;
  }
  .title .lead { background: var(--duck-egg-deep); width: 175px; }
  .title .rest { background: var(--charcoal); flex: 1; }
  .crown { position: absolute; top: 12px; width: 46px; height: 40px; background: var(--duck-egg); border: 1.5px solid var(--outline); border-radius: 4px 4px 6px 6px; }
  .crown.left { left: 187px; }
  .crown.right { left: 958px; }

  .card { position: absolute; background: var(--card-white); text-align: center; color: var(--ink); border: 1px solid var(--outline); }
  .card .band { position: absolute; left: 0; right: 0; bottom: 0; display: flex; align-items: center; justify-content: center; background: var(--duck-egg-pale); border-top: 1px solid var(--outline); }
  .card h2 { font-family: "Open Sans", sans-serif; font-weight: 400; color: var(--teal-ink); font-size: 21px; line-height: 26px; }
  .card p { font-size: 16.5px; line-height: 21px; }

  .card.sell { left: 10px; top: 129px; width: 198px; height: 310px; }
  .card.sell .band { height: 56px; }
  .card.sell h2 { margin-top: 62px; }
  .card.sell p { margin-top: 24px; }

  .card.collect { left: 228px; top: 125px; width: 231px; height: 315px; }
  .card.collect .band { height: 65px; }
  .card.collect h2 { margin-top: 69px; text-align: left; padding-left: 15px; }
  .card.collect p { margin-top: 26px; padding-left: 30px; }

  .card.prepare { left: 474px; top: 125px; width: 231px; height: 315px; }
  .card.prepare .band { height: 60px; }
  .card.prepare h2 { margin-top: 67px; font-size: 22px; }
  .card.prepare p { margin-top: 8px; }

  .card.sold { left: 717px; top: 125px; width: 191px; height: 315px; }
  .card.sold .band { height: 59px; }
  .card.sold h2 { margin-top: 66px; font-size: 22px; }
  .card.sold p { margin-top: 14px; }

  .payout { position: absolute; left: 920px; top: 125px; width: 273px; height: 298px; background: var(--duck-egg); border: 1px solid var(--outline); color: var(--charcoal); }
  .payout .label { position: absolute; font-family: "Oswald", sans-serif; font-weight: 600; font-size: 17px; letter-spacing: .2px; white-space: nowrap; }
  .payout .pocket { left: 94px; top: 24px; }
  .payout .currency { left: 177px; top: 58px; color: var(--outline); font-family: "Archivo Black", sans-serif; font-size: 27px; }
  .payout .donate { left: 0; right: 0; text-align: center; top: 250px; line-height: 21px; }
  .payout .cloud { position: absolute; left: 12px; top: 80px; width: 150px; height: 150px; }
  .payout .arrows { position: absolute; left: 0; top: 0; width: 273px; height: 298px; }
  .payout .halo-spot { position: absolute; left: 216px; top: 218px; width: 50px; height: 50px; border-radius: 50%; background: var(--duck-egg-pale); border: 1.5px solid var(--outline); }

  .step { position: absolute; top: 94px; width: 62px; height: 82px; overflow: visible; }
  .step path { fill: var(--duck-egg); stroke: var(--outline); stroke-width: 1.5; }
  .step text { font-family: "Archivo Black", sans-serif; font-size: 30px; fill: var(--outline); }
  .step.one { left: 78px; } .step.two { left: 314px; } .step.three { left: 556px; }
  .step.four { left: 780px; } .step.five { left: 950px; }
  .icon-fill { fill: var(--duck-egg); stroke: var(--outline); stroke-width: 1.5; stroke-linejoin: round; }
  .smile-spot { width: 46px; height: 46px; border-radius: 50%; background: var(--duck-egg); border: 1.5px solid var(--outline); }
</style>
</head>
<body>
<main class="canvas">
  <div class="crown left" role="img" aria-label="Crown decoration"></div>
  <h1 class="title"><span class="lead">BISPOKE</span><span class="rest">CONCIERGE SERVICE</span></h1>
  <div class="crown right" role="img" aria-label="Crown decoration"></div>

  <section class="card sell">
    <h2>Have items to<br>sell ?</h2>
    <p>brand spanking<br>&nbsp;or nearly new</p>
    <div class="band">
      <svg width="70" height="46" viewBox="0 0 70 46" aria-hidden="true">
        <defs><path id="star" d="M0,-10 L2.9,-3.1 10,-3.1 4.3,1.3 6.5,8.5 0,4.2 -6.5,8.5 -4.3,1.3 -10,-3.1 -2.9,-3.1Z"/></defs>
        <use href="#star" class="icon-fill" x="40" y="12"/>
        <use href="#star" class="icon-fill" x="22" y="26"/>
        <use href="#star" class="icon-fill" x="45" y="34"/>
      </svg>
    </div>
  </section>

  <section class="card collect">
    <h2>Personal Collection</h2>
    <p>we choose the pieces<br>we know thevelora<br>customers will love</p>
    <div class="band">
      <svg width="62" height="54" viewBox="0 0 62 54" aria-hidden="true">
        <path class="icon-fill" d="M31,52 C18,40 2,30 4,15 C6,4 20,1 28,11 L31,15 L34,11 C42,1 56,4 58,15 C60,30 44,40 31,52Z"/>
      </svg>
    </div>
  </section>

  <section class="card prepare">
    <h2>We Prepare</h2>
    <p>your items for sale with<br>thought autheticly &amp;<br>condition checks. from<br>the velora team..</p>
    <p>So You<br>don’t have to</p>
    <div class="band"><div class="smile-spot" role="img" aria-label="Smiley emoticon"></div></div>
  </section>

  <section class="card sold">
    <h2>Once Sold</h2>
    <p>We lovigly prepare<br>the items shipped<br>via tracked<br>services</p>
    <div class="band">
      <svg width="76" height="52" viewBox="0 0 76 52" aria-hidden="true">
        <path class="icon-fill" d="M70,6 C73,3 70,0 66,3 L52,15 L14,10 L9,14 L40,23 L27,36 L15,35 L11,39 L24,43 L31,51 L35,47 L34,38 L47,27 L56,48 L60,43 L55,19Z"/>
      </svg>
    </div>
  </section>

  <section class="payout">
    <div class="label pocket">POCKET THE CASH</div>
    <div class="label currency">$€£</div>
    <svg class="arrows" viewBox="0 0 273 298" aria-hidden="true">
      <defs>
        <marker id="head" markerWidth="6" markerHeight="6" refX="3" refY="3" orient="auto"><path d="M0,0 L6,3 L0,6Z" fill="#111"/></marker>
      </defs>
      <path d="M108,122 C112,95 130,82 150,76" fill="none" stroke="#111" stroke-width="2" marker-end="url(#head)"/>
      <path d="M92,210 C76,222 74,240 86,256" fill="none" stroke="#111" stroke-width="2" marker-end="url(#head)"/>
    </svg>
    <svg class="cloud" viewBox="0 0 150 150" aria-hidden="true">
      <g fill="#111">
        <circle cx="45" cy="45" r="30"/><circle cx="95" cy="40" r="30"/><circle cx="122" cy="78" r="24"/>
        <circle cx="100" cy="112" r="28"/><circle cx="50" cy="112" r="28"/><circle cx="26" cy="78" r="24"/><circle cx="75" cy="78" r="40"/>
      </g>
      <g fill="var(--duck-egg-pale)">
        <circle cx="45" cy="45" r="28.5"/><circle cx="95" cy="40" r="28.5"/><circle cx="122" cy="78" r="22.5"/>
        <circle cx="100" cy="112" r="26.5"/><circle cx="50" cy="112" r="26.5"/><circle cx="26" cy="78" r="22.5"/><circle cx="75" cy="78" r="38.5"/>
      </g>
      <text x="76" y="58" text-anchor="middle" font-family="Archivo Black, sans-serif" font-size="16" fill="var(--charcoal)">YOUR</text>
      <text x="76" y="80" text-anchor="middle" font-family="Archivo Black, sans-serif" font-size="16" fill="var(--charcoal)">PAYMENT</text>
    </svg>
    <div class="halo-spot" role="img" aria-label="Halo emoticon"></div>
    <div class="label donate">DONATE TO CHARITY<br>FULL OR PARTIAL AMOUNT</div>
  </section>

  <svg class="step one" viewBox="0 0 62 82" aria-hidden="true"><path d="M14,1 H48 V44 H61 L31,81 L1,44 H14Z"/><text x="31" y="44" text-anchor="middle">1</text></svg>
  <svg class="step two" viewBox="0 0 62 82" aria-hidden="true"><path d="M14,1 H48 V44 H61 L31,81 L1,44 H14Z"/><text x="31" y="44" text-anchor="middle">2</text></svg>
  <svg class="step three" viewBox="0 0 62 82" aria-hidden="true"><path d="M14,1 H48 V44 H61 L31,81 L1,44 H14Z"/><text x="31" y="44" text-anchor="middle">3</text></svg>
  <svg class="step four" viewBox="0 0 62 82" aria-hidden="true"><path d="M14,1 H48 V44 H61 L31,81 L1,44 H14Z"/><text x="31" y="44" text-anchor="middle">4</text></svg>
  <svg class="step five" viewBox="0 0 62 82" aria-hidden="true"><path d="M14,1 H48 V44 H61 L31,81 L1,44 H14Z"/><text x="31" y="44" text-anchor="middle">5</text></svg>
</main>
</body>
</html>
```